Corporate Design für Onlineshop zum Verkauf von asiatischen Reflexbögen
Zielgruppe
Ich bin Einzelunternehmer (Wendrik Bogensport Jorin Takelberg) und verkaufe in meinem Webshop Asiatische Reflexbögen, häufig auch als Reiterbögen bezeichnet, und alles was der traditionelle Bogenschütze so braucht (z.B. Pfeile, Köcher, Zubehör, etc...)
Aufgabenstellung
Ich suche ein einprägsames Design, das in verschiedenen Größen gut funktioniert und erkennbar ist (sowohl als kleines Logo als auch größer auf Messeständen oder Flyern).
Das Logo sollte am Besten sowohl farbig (z.B. Onlineshop, Visitenkarte, Briefkopf) als auch schwarz/weiß (z.B. als Gravur auf Leder oder Holz) funktionieren.
Wenn die Silouhette eines gespannten typischen Reiterbogens (tatarisch, mongolisch, skytisch oder chinesisch) im Logo drin wäre und ein stilisierter Fuchs, dann würde das den Namen villeicht ganz gut untermalen glaub ich.
Meine Hauptkunden sind Bogenschützen, die vornehmlich mit traditionellen Bögen schießen, sowohl auf dem Platz als auch in der Natur auf dem 3D-Parcours.
Der Name WendRik leitet sich von 'fux = Fuchs' und 'luoga = versteckter Wohnung' ab, heißt also in etwa 'Fuchsbau' so sind hier im Süddeutschen und Österreichischen einige Ortsteile bzw. Einöden benannt, z.B. Wendrik oder Fuchslug in Aschau im Chiemgau.
Meinen Onlineshop baue ich gerade auf, da ist also noch nicht wirklich was zu sehen. Ich brauche daher ein Logo für Shop, Visitenkarte und Briefpapier und ein Design für Visitenkarte und ein Design für Briefpapier/Rechnungen.

```html
<!DOCTYPE html>
<html lang="de">
<head>
<meta charset="utf-8">
<title>WendRik – Corporate Design</title>
<link rel="stylesheet" href="https://fonts.googleapis.com/css2?family=Michroma&family=Poppins:wght@400;500&display=swap">
<style>
:root{
  --bg:#d3d3d3;
  --paper:#ffffff;
  --ink:#1e1e1e;
  --orange:#ee5a0c;
  --navy:#1c2b4a;
  --glass:#dcdcdc;
}
*{box-sizing:border-box;margin:0;padding:0}
html,body{width:1200px;height:2400px;overflow:hidden;background:var(--bg)}
body{position:relative;font-family:"Poppins",sans-serif;color:var(--ink)}
.wordmark{font-family:"Michroma",sans-serif;font-weight:400;color:var(--ink);white-space:nowrap;line-height:1;letter-spacing:.01em}
.wordmark--light{color:var(--paper)}
.mark-dot{border-radius:50%;background:var(--orange)}
.abs{position:absolute}

/* main logo */
.logo-main{left:0;width:1200px;top:80px;display:flex;flex-direction:column;align-items:center;gap:34px}
.logo-main .mark-dot{width:150px;height:150px}
.logo-main .wordmark{font-size:58px}

/* business cards */
.card{background:var(--paper);border-radius:16px;width:492px;height:318px;top:430px;overflow:hidden}
.card--front{left:65px}
.card--back{left:643px}
.card--front .logo{position:absolute;left:0;right:0;top:82px;display:flex;flex-direction:column;align-items:center;gap:18px}
.card--front .mark-dot{width:84px;height:84px}
.card--front .wordmark{font-size:36px}
.double-rule{position:absolute;height:5px;border-top:1.5px solid var(--orange);border-bottom:1.5px solid var(--orange)}
.card--front .site{position:absolute;left:0;right:0;top:288px;text-align:center;font-size:15px;font-weight:500;line-height:1}
.card--back .logo{position:absolute;left:0;right:0;top:14px;display:flex;flex-direction:column;align-items:center;gap:8px}
.card--back .logo .mark-dot{width:56px;height:56px}
.card--back .logo .wordmark{font-size:26px}
.holder{position:absolute;left:22px;top:160px}
.holder .name{font-family:"Michroma",sans-serif;font-size:18px;line-height:1.3}
.holder .title{font-family:"Michroma",sans-serif;font-size:17px;line-height:1.3}
.contact{list-style:none;display:flex;flex-direction:column;gap:8px;color:var(--navy);font-weight:500}
.contact li{display:flex;align-items:center;gap:10px}
.contact .ico{background:var(--orange);border-radius:3px;display:flex;align-items:center;justify-content:center}
.card--back .contact{position:absolute;left:22px;top:228px;font-size:14px}
.card--back .contact .ico{width:19px;height:19px}
.card--back .deco{position:absolute;left:358px;top:160px;width:118px;height:118px}

/* envelopes */
.envelope{background:var(--paper);width:650px;height:330px;overflow:hidden}
.envelope--back{left:70px;top:1230px}
.envelope--back .flap{position:absolute;left:0;top:0}
.envelope--back .site{position:absolute;left:300px;bottom:36px;display:flex;align-items:center;gap:6px;font-size:12px;font-weight:500}
.envelope--front{left:480px;top:860px}
.envelope--front .logo{position:absolute;left:58px;top:150px;display:flex;flex-direction:column;align-items:center;gap:8px}
.envelope--front .mark-dot{width:56px;height:56px}
.envelope--front .wordmark{font-size:28px}
.envelope--front .window{position:absolute;left:400px;top:90px;width:190px;height:78px;border-radius:8px;background:linear-gradient(160deg,#e8e8e8,#cfcfcf 55%,#e4e4e4)}
.envelope--front .band{position:absolute;left:0;right:0;bottom:0;height:9px;background:var(--orange)}

/* letterhead */
.letterhead{background:var(--paper);left:58px;top:1612px;width:507px;height:718px}
.letterhead .contact{position:absolute;left:26px;top:60px;font-size:9.5px;gap:5px}
.letterhead .contact .ico{width:13px;height:13px}
.letterhead .logo{position:absolute;right:26px;top:30px;display:flex;flex-direction:column;align-items:center;gap:10px}
.letterhead .mark-dot{width:66px;height:66px}
.letterhead .wordmark{font-size:27px}
.letterhead .band{position:absolute;left:0;right:0;bottom:0;height:8px;background:var(--orange)}

/* folder */
.folder{background:var(--ink);left:636px;top:1612px;width:508px;height:718px}
.folder .band{position:absolute;left:0;right:0;top:0;height:7px;background:var(--orange)}
.folder .logo{position:absolute;left:0;right:0;top:252px;display:flex;flex-direction:column;align-items:center;gap:34px}
.folder .mark-dot{width:126px;height:126px}
.folder .wordmark{font-size:47px}
.folder .site{position:absolute;left:0;right:0;bottom:14px;text-align:center;color:var(--paper);font-size:10px;font-weight:500}
</style>
</head>
<body>

<!-- main logo -->
<section class="abs logo-main">
  <span class="mark-dot"></span>
  <span class="wordmark">WendRik</span>
</section>

<!-- business card front -->
<article class="abs card card--front">
  <div class="logo">
    <span class="mark-dot"></span>
    <span class="wordmark">WendRik</span>
  </div>
  <span class="double-rule" style="left:0;width:166px;top:298px"></span>
  <span class="site">www.website.com</span>
  <span class="double-rule" style="right:0;width:166px;top:298px"></span>
</article>

<!-- business card back -->
<article class="abs card card--back">
  <div class="logo">
    <span class="mark-dot"></span>
    <span class="wordmark">WendRik</span>
  </div>
  <span class="double-rule" style="left:0;right:0;top:128px"></span>
  <div class="holder">
    <p class="name">Your Name</p>
    <p class="title">Title</p>
  </div>
  <ul class="contact">
    <li><span class="ico"><svg width="11" height="11" viewBox="0 0 24 24"><path d="M6.6 10.8a15 15 0 0 0 6.6 6.6l2.2-2.2c.3-.3.7-.4 1-.2 1.1.4 2.3.6 3.6.6.6 0 1 .4 1 1V20c0 .6-.4 1-1 1A17 17 0 0 1 3 4c0-.6.4-1 1-1h3.5c.6 0 1 .4 1 1 0 1.3.2 2.5.6 3.6.1.3 0 .7-.2 1z" fill="#fff"/></svg></span>012-345-6789</li>
    <li><span class="ico"><svg width="11" height="11" viewBox="0 0 24 24"><rect x="2" y="5" width="20" height="14" rx="1" fill="#fff"/><path d="M2 6l10 7 10-7" stroke="#ee5a0c" stroke-width="2" fill="none"/></svg></span>Youremail.com</li>
    <li><span class="ico"><svg width="12" height="12" viewBox="0 0 24 24" fill="none" stroke="#fff" stroke-width="1.6"><circle cx="12" cy="12" r="9"/><ellipse cx="12" cy="12" rx="4" ry="9"/><path d="M3 12h18M5 7h14M5 17h14"/></svg></span>www.website.com</li>
  </ul>
  <span class="deco mark-dot"></span>
</article>

<!-- envelope back -->
<article class="abs envelope envelope--back">
  <svg class="flap" width="650" height="110" viewBox="0 0 650 110">
    <path d="M0 0H650V18C470 40 300 60 120 95 60 106 30 100 0 55Z" fill="#1e1e1e"/>
  </svg>
  <span class="site"><svg width="13" height="13" viewBox="0 0 24 24" fill="none" stroke="#1e1e1e" stroke-width="1.6"><circle cx="12" cy="12" r="9"/><ellipse cx="12" cy="12" rx="4" ry="9"/><path d="M3 12h18"/></svg>www.website.com</span>
</article>

<!-- envelope front -->
<article class="abs envelope envelope--front">
  <div class="logo">
    <span class="mark-dot"></span>
    <span class="wordmark">WendRik</span>
  </div>
  <span class="window"></span>
  <span class="band"></span>
</article>

<!-- letterhead -->
<article class="abs letterhead">
  <ul class="contact">
    <li><span class="ico"><svg width="8" height="8" viewBox="0 0 24 24"><path d="M6.6 10.8a15 15 0 0 0 6.6 6.6l2.2-2.2c.3-.3.7-.4 1-.2 1.1.4 2.3.6 3.6.6.6 0 1 .4 1 1V20c0 .6-.4 1-1 1A17 17 0 0 1 3 4c0-.6.4-1 1-1h3.5c.6 0 1 .4 1 1 0 1.3.2 2.5.6 3.6.1.3 0 .7-.2 1z" fill="#fff"/></svg></span>012-345-6789</li>
    <li><span class="ico"><svg width="8" height="8" viewBox="0 0 24 24"><rect x="2" y="5" width="20" height="14" rx="1" fill="#fff"/><path d="M2 6l10 7 10-7" stroke="#ee5a0c" stroke-width="2" fill="none"/></svg></span>Youremail.com</li>
    <li><span class="ico"><svg width="9" height="9" viewBox="0 0 24 24" fill="none" stroke="#fff" stroke-width="1.8"><circle cx="12" cy="12" r="9"/><ellipse cx="12" cy="12" rx="4" ry="9"/><path d="M3 12h18"/></svg></span>www.website.com</li>
  </ul>
  <div class="logo">
    <span class="mark-dot"></span>
    <span class="wordmark">WendRik</span>
  </div>
  <span class="band"></span>
</article>

<!-- presentation folder -->
<article class="abs folder">
  <span class="band"></span>
  <div class="logo">
    <span class="mark-dot"></span>
    <span class="wordmark wordmark--light">WendRik</span>
  </div>
  <span class="site">www.website.com</span>
</article>

</body>
</html>
```